Rapidly Growing Small Management Consulting Firm seeking Letterhead/Business Proposal Template

Small Management Consulting Firm in need of Stationery/Business Proposal Template/Business Card for communicating and corresponding to formal Government Statement of Work (SOWs) Request for Proposals (RFP), general business correspondences and engagements with private industry clients. I am in need of company letterhead/stationery and proposal package of documents that follow the same theme in MS Word or a format that I can easily edit to readily respond quickly to business inquiries.

Consulting Firm small business start-up. Minority woman-owned rapidly growing consulting firm based in Washington, DC metropolitan area with a target market of the local and federal government. Would like see some area government images such as buildings or monuments. Looking for something eye-catching and creates a strong presence. The final design should communicate our numerous service offerings.

Target Market(s)

Local State, Federal Government and Private Industry clients and (Business-to-Business (B2B)

Industry/Entity Type

Management Consulting

Number of Pages Required

3 page

Font styles to use
Serif
Sans Serif
Other font styles liked:
• Arial, Calibri, Cambria and Times Roman

Colors
3176b5
ffffff
ec1f27
85abd2
cfdeed

Requirements
Must have
• WEBSITE: PLEASE TAKE A LOOK AT SOME OF THE IMAGES PROVIDED. I AM EXTREMELY INTERESTED IN IMAGE #16. IF SOMETHING LIKE THIS CAN BE DONE FOR THE WEBSITE LANDING PAGE WITH A WASHINGTON, DC OR MONUMENTAL BACKDROP OR BACKGROUND. WOULD LIKE TO USE THE IMAGE OF AFRICAN AMERICAN WOMAN IN FRONT ALONG WITH ANY OTHER DIVERSE STOCK IMAGES BEHIND HER. PLEASE USE A LIGHTER AND BRIGHTER BACKGROUND.
• FOR WEBSITE IMAGE INSPIRATION
• PLEASE TAKE A LOOK @ http://www.tendralux.com/
• http://brimwaltsite.net/wp-demo/lawfirm/practice-area-01/
• Website: I would like to see general information pages such as Home Page, About US, Services Offered and Careers and Contact Us pages. Must have consistent theme in line with existing Capability Statement.
• FOR COMPANY LETTERHEAD/PROPOSAL/PRESENTATION PAGES:
• MUST FOLLOW SAME THEME. MUST BE IN MS WORD OR FORM THAT CAN BE EASILY EDITABLE. PLEASE SEE UPLOADED "PROPOSAL-PRESENTATION COVER PAGE" IMAGES FOR ADDITIONAL INSPIRATION. I VERY MUCH LIKE IMAGES PPCP #4 AND PPCP#5.
• Must include a multi-use company cover page for proposals and business presentations.
• For letterhead and please incorporate existing logo into design. Company colors gray and blue. Must have the functionality to format page numbering, consistent company information throughout document in headers and footers and will need a customizable company cover page that can be used for proposals and presentations.
• Please do not make the header and footer borders too large as I have to be able to input company information into the space. Some responses have set page limits so it is very important to preserve as much space as possible.
• Please use updated company address: 482 Harrowgate Lane, La Plata, MD 20731
Nice to have
• Illustration of images that show professional women and minority (african-american) woman in business or professional settings. Women business owners preferably. Classic and very professional appearance. Even though we are a small firm I would like to design to give the impression and feel of doing business with a large management firm. Or large firm appeal. Also incorporate image of contract signing as our main line of business is acquisitions which is much like the services of a law firm.
• 01/21/17. Added some images of women business owner examples.
Should not have
• Misspellings, images of professionals without business attire.

```html
<!DOCTYPE html>
<html lang="en">
<head>
<meta charset="utf-8">
<title>Halvern Acquisition Advisors – Stationery &amp; Proposal Set</title>
<link href="https://fonts.googleapis.com/css2?family=Open+Sans:ital,wght@0,300;0,400;0,600;0,700;1,400&display=swap" rel="stylesheet">
<style>
:root{
  --bg:#a7a7a7;
  --paper:#ffffff;
  --navy:#1d4a86;
  --blue:#2d62a3;
  --link:#3a78c2;
  --pale:#cfe0f0;
  --mist:#e4ecf5;
  --grey:#6e7682;
  --rule:#9fb6d2;
  --ink:#333a44;
  --soft:#8fa7c2;
  --client:#5f8f8a;
}
*{box-sizing:border-box;margin:0;padding:0}
html,body{width:1200px;height:1200px;overflow:hidden;background:var(--bg)}
body{font-family:"Open Sans",Arial,sans-serif;color:var(--ink)}
.stage{position:relative;width:1500px;height:1500px;transform:scale(.8);transform-origin:0 0}
.page{position:absolute;width:328px;height:424px;background:var(--paper);box-shadow:4px 5px 8px rgba(0,0,0,.28);overflow:hidden}
.letterhead{left:571px;top:41px;width:359px;height:463px}
.r2{top:543px}.r3{top:1005px}
.c1{left:46px}.c2{left:407px}.c3{left:768px}.c4{left:1136px}

.mark{text-align:center;color:var(--navy);line-height:1}
.mark .name{font-weight:700;letter-spacing:.16em;display:block}
.mark .sub{display:block;color:var(--blue);letter-spacing:.14em;font-weight:600;margin-top:2px}
.mark .dot{display:inline-block;background:var(--blue);border-radius:50%;vertical-align:middle}

.page-head{position:absolute;left:0;right:0;top:12px;border-top:1px solid var(--rule);padding-top:3px}
.page-head h1{border-top:1px solid var(--rule);font-size:11.5px;font-weight:700;color:var(--navy);text-align:center;padding:5px 0 4px;border-bottom:1px solid var(--rule);letter-spacing:.01em}

.page-foot{position:absolute;left:0;right:0;bottom:0;height:22px}
.page-foot .band{position:absolute;left:0;bottom:6px;width:248px;height:8px;background:var(--blue);clip-path:polygon(0 0,100% 0,96% 100%,0 100%)}
.page-foot .band span{font-size:4.2px;color:#fff;position:absolute;left:28px;top:1.5px}
.page-foot .shade{position:absolute;left:240px;bottom:6px;width:14px;height:8px;background:#9aa5b3;clip-path:polygon(40% 0,100% 0,60% 100%,0 100%)}
.page-foot .logo{position:absolute;left:250px;bottom:3px;width:50px;font-size:6px;font-weight:700;letter-spacing:.14em;color:var(--navy);text-align:center}
.page-foot .num{position:absolute;right:0;bottom:6px;width:30px;height:8px;background:var(--blue);color:#fff;font-size:6px;text-align:center;line-height:8px;clip-path:polygon(15% 0,100% 0,100% 100%,0 100%)}

.body{position:absolute;left:29px;right:29px;top:50px;font-size:4.6px;line-height:1.72}
.body p{margin-bottom:5px}
.sub-head{font-size:8px;font-weight:300;color:var(--grey);margin:9px 0 3px}
.lead{color:var(--navy);font-weight:700}
.link{color:var(--link)}

.letterhead .mark{position:absolute;top:26px;left:0;right:0}
.lh-foot{position:absolute;left:0;right:0;bottom:0;height:24px}
.lh-foot .contact{position:absolute;left:32px;bottom:13px;font-size:4.2px;color:var(--grey);display:flex;gap:10px;align-items:center}
.lh-foot .contact i{display:inline-block;width:5px;height:4px;background:var(--blue);margin-right:2px;vertical-align:middle}
.lh-foot .contact b{font-weight:400;border-left:1px solid var(--rule);padding-left:6px}
.lh-foot .band{position:absolute;left:0;bottom:0;width:270px;height:9px;background:var(--blue);clip-path:polygon(0 0,100% 0,97% 100%,0 100%)}
.lh-foot .grey{position:absolute;right:0;bottom:0;width:96px;height:9px;background:#9aa5b3;clip-path:polygon(6% 0,100% 0,100% 100%,0 100%)}
.lh-foot .line{position:absolute;left:0;right:0;bottom:11px;border-top:1px solid var(--rule)}

.cover .url{position:absolute;right:22px;top:9px;font-size:4.2px;color:var(--grey)}
.cover .presented{position:absolute;top:84px;left:0;right:0;text-align:center;font-size:17.5px;font-weight:400;color:var(--blue)}
.cover .client{position:absolute;top:120px;left:0;right:0;text-align:center;font-size:21px;font-weight:300;color:var(--client)}
.cover .band{position:absolute;left:0;right:0;top:190px;height:128px;background:var(--blue)}
.cover .date{position:absolute;right:30px;top:256px;color:#fff;font-size:12px;font-weight:600}
.cover .date sup{font-size:7px}
.cover .mark{position:absolute;left:0;right:0;top:358px}

.toc-title{font-size:11px;font-weight:300;color:var(--grey);margin-bottom:7px}
.toc li{list-style:none;display:flex;align-items:center;height:10.6px;font-size:4.6px}
.toc .lead-dots{flex:1;border-bottom:1px dotted #8c96a3;margin:0 4px;height:1px}
.toc .pg{width:22px;height:7px;background:var(--pale);color:var(--navy);font-size:4.4px;text-align:center;line-height:7px;font-weight:600}

.grid{display:grid;grid-template-columns:140px 48px 58px;gap:2px;justify-content:start;margin:6px 0 9px}
.grid div{height:8px;font-size:4.3px;line-height:8px;padding-left:5px;background:var(--pale)}
.grid .n{text-align:center;padding-left:0}
.grid .th{background:var(--blue);color:#fff;text-align:center;font-weight:600;padding-left:0}
.grid .ph{background:#d8dde4;color:var(--blue);font-weight:600;grid-column:1/-1}
.grid .tot{background:#d8dde4;font-weight:700}
.grid .grand{background:#b7c9de;color:var(--navy);font-weight:700}
.grid2{grid-template-columns:170px 98px}

ul.sq{list-style:none;margin:0 0 5px}
ul.sq>li{padding-left:7px;position:relative;margin-bottom:1px}
ul.sq>li::before{content:"";position:absolute;left:0;top:2.4px;width:3px;height:3px;background:var(--navy)}
ul.tri{list-style:none;margin:1px 0 4px 28px}
ul.tri li{position:relative;padding-left:6px;color:var(--link)}
ul.tri li::before{content:"";position:absolute;left:0;top:2px;border-left:3.5px solid var(--navy);border-top:2px solid transparent;border-bottom:2px solid transparent}

.cols{display:grid;grid-template-columns:1fr 1fr;gap:12px}
.svc{border-left:1px solid var(--blue);padding-left:4px}
.svc h3{font-size:7px;font-weight:400;color:var(--link);margin-bottom:1px}
.svc li{color:var(--navy);font-weight:600}

.thanks .halo{position:absolute;left:84px;top:112px;width:160px;height:160px;border-radius:50%;background:var(--mist)}
.thanks .ty{position:absolute;top:292px;left:0;right:0;text-align:center;font-size:23px;font-weight:600;color:var(--soft)}
.thanks .foot{position:absolute;left:72px;right:20px;top:388px;display:flex;align-items:center;gap:12px;font-size:4.2px;color:var(--link);line-height:1.6}
.thanks .foot .mark{font-size:7px}
.thanks .foot .col{border-left:1px solid var(--rule);padding-left:5px}
</style>
</head>
<body>
<div class="stage">

  <section class="page letterhead">
    <div class="mark"><span class="name" style="font-size:13px"><span class="dot" style="width:5px;height:5px;margin-right:4px"></span>HALVERN</span><span class="sub" style="font-size:3.6px">ACQUISITION ADVISORS</span></div>
    <div class="lh-foot">
      <div class="line"></div>
      <div class="contact"><span><i></i>+1 234 567 8901</span><span><i></i>+1 234 567 8901</span><b>Address Line 1, Area, City Name, Area Name, 1234</b></div>
      <div class="band"></div><div class="grey"></div>
    </div>
  </section>

  <section class="page r2 c1 cover">
    <div class="url">www.halvern.com</div>
    <div class="presented">Proposal Presented to</div>
    <div class="client">verdaNation</div>
    <div class="band"></div>
    <div class="date">4<sup>th</sup> February 2017</div>
    <div class="mark"><span class="name" style="font-size:19px"><span class="dot" style="width:7px;height:7px;margin-right:5px"></span>HALVERN</span><span class="sub" style="font-size:4.6px">ACQUISITION ADVISORS</span></div>
  </section>

  <section class="page r2 c2">
    <header class="page-head"><h1>TABLE OF CONTENTS</h1></header>
    <div class="body" style="top:60px">
      <div class="toc-title">Contents</div>
      <ul class="toc">
        <li>Table of Contents<span class="lead-dots"></span><span class="pg">01</span></li>
        <li>Executive Summary<span class="lead-dots"></span><span class="pg">02</span></li>
        <li>Our Understanding of Your Needs<span class="lead-dots"></span><span class="pg">02</span></li>
        <li>Our Recommendations<span class="lead-dots"></span><span class="pg">03</span></li>
        <li>Our Approach<span class="lead-dots"></span><span class="pg">05</span></li>
        <li>Budget and Timeframe<span class="lead-dots"></span><span class="pg">07</span></li>
        <li>Appendix A: About Cedar Falls<span class="lead-dots"></span><span class="pg">10</span></li>
        <li>Appendix B: Selected Client List<span class="lead-dots"></span><span class="pg">10</span></li>
        <li>Appendix C: Our Capabilities<span class="lead-dots"></span><span class="pg">11</span></li>
        <li>Appendix D: Our Process<span class="lead-dots"></span><span class="pg">12</span></li>
      </ul>
    </div>
    <footer class="page-foot"><div class="band"><span>www.halvern.com</span></div><div class="shade"></div><div class="logo">HALVERN</div><div class="num">01</div></footer>
  </section>

  <section class="page r2 c3">
    <header class="page-head" style="top:8px"><h1>EXECUTIVE SUMMARY</h1></header>
    <div class="body" style="top:46px">
      <p>We are excited to present verdaNation with our proposal for CloudLedger implementation and website integration support. Since our company's inception in 2008 we have been at the forefront of implementing and integrating CloudLedger with Nodewell based websites, email service providers and other applications to support the online fundraising, marketing and program work of nonprofit organizations.</p>
      <div class="sub-head">What We're Proposing</div>
      <p>We propose that verdaNation move forward in a phased CloudLedger implementation approach to support the PulseWay launch (currently scheduled for March 21st).</p>
      <div class="sub-head">What's in our Proposal</div>
      <p>Within this proposal we will address NWSA's verdaNation specific requirements and how they translate from a SaaS solution to a best of breed model and we will provide more information on the features, benefits, and architecture of Keystone Suite. We welcome the opportunity to discuss Keystone Suite in more detail, and to provide a demonstration of the power that comes with a best of breed approach, developed by industry experts and adopted by the most innovative online nonprofits.</p>
      <p>If you have any questions or comments, please feel free to contact us directly.</p>
      <p>Sincerely,</p>
      <p style="margin-top:9px;margin-bottom:0"><b>RJ Marlow</b><br>Partner and Co-Founder<br><span class="link">rj.marlow@cedarfalls.com</span><br>(512) 555-0148</p>
    </div>
    <footer class="page-foot" style="bottom:4px"><div class="band"><span>www.halvern.com</span></div><div class="shade"></div><div class="logo">HALVERN</div><div class="num">02</div></footer>
  </section>

  <section class="page r2 c4">
    <header class="page-head" style="top:9px"><h1>BUDGET AND TIMEFRAME</h1></header>
    <div class="body" style="top:52px;font-size:4.4px;line-height:1.68">
      <div class="sub-head" style="margin-top:3px">Implementation Estimate</div>
      <p>The bulk of the implementation costs will be defined by discovery. Based on similar CRM implementation projects, we feel expect that the CRM side will be somewhere between 200 and 300 hours, give or take. The wide swing in hours in phase one is related currently to the ill-defined nature of both the integration needs and our role in the integration project. Our focus in discovery (as mentioned above) will be to nail down and finalize those requirements and our role as it relates to what is needed to integrate the sites with the CRM.</p>
      <div class="grid">
        <div class="th">Task</div><div class="th">Hours</div><div class="th">Cost</div>
        <div>Discovery</div><div class="n">40</div><div class="n">$8,000</div>
        <div class="ph">Phase 1</div>
        <div>Discovery</div><div class="n">20-40</div><div class="n">$8,000</div>
        <div>Discovery</div><div class="n">20-40</div><div class="n">$8,000</div>
        <div>Discovery</div><div class="n">20-40</div><div class="n">$8,000</div>
        <div class="tot">Total Phase 1</div><div class="tot n">80-240</div><div class="tot n">$16,800-40,000</div>
        <div class="ph">Phase 2</div>
        <div>Discovery</div><div class="n">20-40</div><div class="n">$8,000</div>
        <div class="tot">Total Phase 2</div><div class="tot n">80-240</div><div class="tot n">$16,800-40,000</div>
        <div class="grand">Total Estimated Implementation Cost</div><div class="grand n">220-480</div><div class="grand n">$44,000-96,000</div>
      </div>
      <div class="sub-head" style="margin-top:0">Project Timeline</div>
      <p>Based on the information we have at our disposal, the March 21st launch date doesn't seem a realistic goal to get both the work done needed to provide the foundation for the future CRM instance and the integration given the state of apparent flux of the requirements. That said, we feel it prudent to proceed with discovery before committing to or pushing that date. We are currently estimating that the first phase will take somewhere between 7 and 12 weeks (including discovery) to complete.</p>
      <div class="grid grid2">
        <div class="th">Task</div><div class="th">Weeks to Complete</div>
        <div>Discovery</div><div class="n">1-2</div>
        <div>Phase 1</div><div class="n">6-10</div>
        <div>Phase 2</div><div class="n">8-12</div>
        <div class="tot">Total Number of Weeks</div><div class="tot n"></div>
      </div>
    </div>
    <footer class="page-foot"><div class="band"><span>www.halvern.com</span></div><div class="shade"></div><div class="logo">HALVERN</div><div class="num">05</div></footer>
  </section>

  <section class="page r3 c1">
    <header class="page-head" style="top:8px"><h1>OUR UNDERSTANDING OF YOUR NEEDS</h1></header>
    <div class="body" style="top:46px;font-size:4.4px;line-height:1.68">
      <p>In the last two weeks of January 2014 we conducted high level conversations both with your staff and your technology partner Signalry. As a result of those conversations we've been able to gather the following high level goals for your project:</p>
      <div class="sub-head" style="margin-top:4px;line-height:1.15">CloudLedger must be in place to support PulseWay at launch and as the program evolves</div>
      <p class="lead">The most critical aspect of this implementation both in terms of time sensitivity as well as functionality is centered around the support for the PulseWay project. Our current understanding of this project and how it relates to CloudLedger is as follows:</p>
      <ul class="sq">
        <li>PulseWay will be comprised of a series of websites focused on organizing institutions and individuals within six specific community sectors with the goal of increased institutional and public support to help the country become better prepared to minimize the risks and maximize opportunities of changing climate.</li>
        <li>The primary goals of the CRM application are:
          <ul class="tri">
            <li>capture information of individuals and organizations (along with their respective roles)</li>
            <li>track their progress on their site specific to-do lists and site interactions</li>
            <li>allow verdaNation to push out next steps (ideally in an automated style) related to their to do list progress and online interactions</li>
            <li>infuse verdaNation's online and offline marketing program with useful segmentation information</li>
            <li>natively integrate with both the PulseWay family of sites as well as verdaNation's email service provider of choice</li>
          </ul></li>
        <li>The data architecture must be well defined but flexible to support the core needs of the sites as well as anticipated needs in the future.
          <ul class="tri">
            <li>For instance, the faith based site may collect a "denomination" field, while other sites may not collect that field.</li>
            <li>Future interactions outside of the to-do list may become necessary to track and verdaNation will need a systemic way to capture those interactions, be able to segment on them and potentially provide automated marketing around those similar to the to-do list</li>
          </ul></li>
        <li>The information collected from the PulseWay sites must be combined with current information held within verdaNation and provide a holistic view of institutions and individuals.</li>
      </ul>
    </div>
    <footer class="page-foot"><div class="band"><span>www.halvern.com</span></div><div class="shade"></div><div class="logo">HALVERN</div><div class="num">03</div></footer>
  </section>

  <section class="page r3 c2">
    <header class="page-head" style="top:8px"><h1>OUR APPROACH</h1></header>
    <div class="body" style="top:46px;font-size:4.4px;line-height:1.68">
      <div class="sub-head" style="margin-top:2px">Discovery</div>
      <p>Given the timeline, the discovery will be brief and focused on the following goals:<br>1) Define the minimum viable product to support the PulseWay launch<br>2) Define the future state CRM, specifically highlighting areas that must be in place for Phase 1 launch<br>3) Define data maintenance tasks needed<br>4) Determine scope of Cedar Falls involvement in integration<br>5) Level set, finalize current scope and estimates and produce phase 1 implementation statement of work<br>6) Prototype solutions where needed to assist in clarifying functionality as well as defining and refining various approaches to specific problems</p>
      <div class="cols">
        <div>
          <div class="sub-head">Phase 1 Implementation</div>
          <span class="link">1) Implement the minimum viable product as defined in discovery. Discovery including</span><br>a. Object and field definition<br>b. Workflow rules and automation to power online marketing<br>c. Email service provider integration and consulting<br>d. Reporting and dashboards to support PulseWay<br><span class="link">2) Assist in website integration as defined in discovery<br>3) Port existing data to the new data structure<br>4) Develop the underpinning for the future CRM</span><br>a. Establish the Core Starter Kit implementation and configuration<br>b. Begin the data mapping process for phase 2
        </div>
        <div>
          <div class="sub-head">Phase 2 Implementation</div>
          <span class="link">1) Port the old development instance to the new instance</span><br>a. Complete data mapping<br>b. Establish any remaining field and object definition<br>c. Create additional workflow rules and automation as necessary<br>d. Migrate the data<br>e. Decommission the old instance<br><span class="link">2) Establish reporting and dashboards<br>3) Configure permissions and any additional application integration<br>4) Develop roadmap for anticipated future needs</span>
        </div>
      </div>
      <div class="sub-head">Training, Support and Launch</div>
      <span class="link">1) Train staff at milestones within each phase<br>2) Document custom code and/or configuration as needed<br>3) Provide both run-time and post launch support as needed</span>
    </div>
    <footer class="page-foot"><div class="band"><span>www.halvern.com</span></div><div class="shade"></div><div class="logo">HALVERN</div><div class="num">04</div></footer>
  </section>

  <section class="page r3 c3">
    <header class="page-head" style="top:8px"><h1>APPENDIX C : OUR CAPABILITIES</h1></header>
    <div class="body" style="top:46px;font-size:4.4px;line-height:1.68">
      <p>At Cedar Falls, we've lived and breathed every stage of the nonprofit lifecycle: from technology strategy to organizational development, from mission-driven work to supporter engagement, from online to offline communications, from RFP to finished product. Although our primary charge is the effective selection and implementation of marketing technologies, a big-picture perspective on organizational success is embedded in our DNA.</p>
      <p>Our clients engage us to help them with a diverse array of strategic and technical work. We regularly support organizations with:</p>
      <div class="cols" style="grid-template-columns:1.55fr 1fr;margin-top:12px">
        <div>
          <div class="sub-head" style="margin-top:0">Technology Assessment &amp; Strategy</div>
          <p>Because of our commitment to both best-of-breed and open source technologies, organizations often ask us to help recommend a comprehensive set of solutions beyond online marketing and fundraising. We bring all of our industry knowledge to bear in assessing your organization's model, staffing and skillset, legacy toolset, strategic objectives, and the current challenges to your growth, and then recommend a combination of solutions that can be tailored for your precise needs.</p>
          <div class="sub-head">Keystone Suite Implementation</div>
          <p>While Keystone Suite is a truly open-source solution, many organizations who choose Keystone Suite as their online marketing and fundraising solution also choose to work with us as their implementation partner. We get each organization up and running with an advanced set of supporter engagement forms, as well as deep CRM integration, tailoring each setup around an org's unique priorities for social and mobile marketing, sustainer engagement, analytics and measurement, and other core objectives.</p>
        </div>
        <div style="padding-top:2px">
          <div class="svc"><h3>Services Include:</h3><ul class="sq"><li>Stakeholder interviews</li><li>Organizational resource analysis</li><li>Current toolset assessment</li><li>Technology recommendations</li><li>Actionable rollout plan</li><li>Staffing &amp; process strategy</li></ul></div>
          <div class="svc" style="margin-top:48px"><h3>Services Include:</h3><ul class="sq"><li>Technical solution design</li><li>Donation form buildout</li><li>Engagement form buildout</li><li>CRM integration</li><li>Custom dashboard development</li><li>Phased plan for marketing growth</li></ul></div>
        </div>
      </div>
    </div>
    <footer class="page-foot"><div class="band"><span>www.halvern.com</span></div><div class="shade"></div><div class="logo">HALVERN</div><div class="num">06</div></footer>
  </section>

  <section class="page r3 c4 thanks">
    <div class="halo" role="img" aria-label="Faint decorative brand backdrop"></div>
    <div class="ty">Thank You</div>
    <div class="foot">
      <div class="mark"><span class="name">HALVERN</span></div>
      <div class="col">Addressline 1 Street Name<br>Area Code, City Name</div>
      <div class="col">info@halvern.com<br>www.halvern.com</div>
    </div>
  </section>

</div>
</body>
</html>
```